"The Plumeworks" nails, eyelash extensions and hair extensions. Need an eye catching design for bu

Need an eye catching design focusing on eyelash extensions, nail extensions and hair extensions. I like the colour green, black, glitter, pink?! need the design to be innovative and 'POP'. I'd like more emphasis on lashes and nails.
I'd like the business name and my phone number on the front of card.
Would really like something different and unique.
"The Plumeworks"
Nails, Eyelash & Hair Extensions
Mira
0417265903

Target Market(s)

20-40

Industry/Entity Type

Beauty Salon

Contact Information for Business Card

Id like my business name, My name and phone number on the front of card
"The Plumeworks".
Mira.
0417265903.
Id like some catchy design involving long lashes with possibly glitter, long hair and nails. Id like the lashes to be the first thing you see at first glance. I'm open to your creative flair. Just need the business card design to 'POP'! I like the colours green, black, pink, silver or gold glitter. wether it's pop art, 3d drawn pictures, isolated pics of lash, nails or hair, card design could be in black and white with isolated colours added..i'm open to your creative flair. use a font which stands out and easy to read.
(The back of the card will be used for writing appointment times.)

Font styles to use
Serif

Colors
6b449b
e667a6
25b39d

Requirements
Must have
• Long lashes, hair, nails.
• one sided
Nice to have
• bright catchy colours, innovative, uniqueness

```html
<!DOCTYPE html>
<html lang="en">
<head>
<meta charset="utf-8">
<title>The Plumeworks — Business Card</title>
<link href="https://fonts.googleapis.com/css2?family=Dosis:wght@400;600&family=Quicksand:wght@400&display=swap" rel="stylesheet">
<style>
  :root {
    --page-bg: #e9e9e7;
    --card-pink: #ec1f78;
    --ink-dark: #2a0f1c;
    --ink-light: #ffffff;
    --art-light: #f3b6cf;
    --art-mid: #ec1f78;
  }
  html, body {
    margin: 0;
    padding: 0;
    width: 1200px;
    height: 1021px;
    overflow: hidden;
    background: var(--page-bg);
  }
  .canvas {
    position: relative;
    width: 1200px;
    height: 1021px;
  }
  .business-card {
    position: absolute;
    left: 110px;
    top: 227px;
    width: 980px;
    height: 567px;
    background: var(--card-pink);
    border-radius: 4px;
    box-shadow: 0 10px 30px rgba(0,0,0,0.18);
    overflow: hidden;
  }
  .portrait-art {
    position: absolute;
    left: 360px;
    top: 96px;
    width: 240px;
    height: 190px;
    border-radius: 6px;
    background: radial-gradient(ellipse at 45% 45%, var(--art-light) 0%, var(--art-mid) 78%);
  }
  .brand-name {
    position: absolute;
    left: 0;
    right: 0;
    top: 300px;
    margin: 0;
    text-align: center;
    font-family: "Dosis", sans-serif;
    font-size: 56px;
    letter-spacing: 2px;
    line-height: 1;
  }
  .brand-name .brand-article {
    color: var(--ink-light);
    font-weight: 400;
  }
  .brand-name .brand-word {
    color: var(--ink-dark);
    font-weight: 600;
  }
  .contact-line {
    position: absolute;
    left: 0;
    right: 0;
    top: 388px;
    margin: 0;
    text-align: center;
    font-family: "Quicksand", sans-serif;
    font-size: 38px;
    letter-spacing: 1px;
  }
  .contact-line .owner-name { color: var(--ink-light); }
  .contact-line .phone-number { color: var(--ink-dark); }
</style>
</head>
<body>
<main class="canvas">
  <section class="business-card">
    <div class="portrait-art" role="img" aria-label="Line drawing of a woman in profile with long flowing hair and a hand with long nails near her face"></div>
    <h1 class="brand-name"><span class="brand-article">The </span><span class="brand-word">Plumeworks</span></h1>
    <p class="contact-line"><span class="owner-name">Mira.</span> <span class="phone-number">0417265903</span></p>
  </section>
</main>
</body>
</html>
```